CV brochure for Top Management Position

I need me to introduce myself a brochure design for a CV brochure in. So sort of a resume in booklet format. The design should be serious for a convey on the other, the viewer that I stand for the new world of digitization. The brochure is intended to convey that I am a "Digital Leader". With the brochure boards, boards of directors and decision makers of enterprises should pay attention to my person. It must not be a 0815 design of the rod. The design should already be addressed with the front page of the topic Digital Leader, since the front page usually is the decisive criterion whether to continue dealing with the person or not. I am now CIO (IT manager) and wants to move with the brochure myself from this technique corner out and thus make it interesting for other positions. The positions are in absolute top management, the board, management, supervisory anchored and deal primarily with the digital transformation and the new digital world. So should appear with security on the front page a concise picture of me. but I am also very open to any alternative proposal brochure. Here you can see my current CV with picture and the basic content. The brochure is even more responsive to the social skills and not only to the technical projects implemented as before.

Target Market(s)

Top management, CxO level, supervisory boards, large companies, large Mittlestandsunternehmen

Industry/Entity Type

Management

Font styles to use
Serif
Sans Serif

Requirements
Must have
• see description
Nice to have
• see description
Should not have
• see description

```html
<!DOCTYPE html>
<html lang="de">
<head>
<meta charset="utf-8">
<title>Digital Leader – Lebenslauf</title>
<link rel="stylesheet" href="https://fonts.googleapis.com/css2?family=Roboto+Condensed:wght@400;700&family=Lato:wght@400;700&display=swap">
<style>
:root{
  --blue:#12a7ec;
  --ink:#2b2b2b;
  --text:#333;
  --grey:#e6e6e6;
  --band:#2a2a2a;
  --page:#fff;
  --bg:#fff;
}
*{box-sizing:border-box;margin:0;padding:0}
html,body{width:1200px;height:909px;overflow:hidden;background:var(--bg)}
body{position:relative;font-family:'Lato',sans-serif;color:var(--text)}
.page{position:absolute;top:72px;width:515px;height:722px;background:var(--page);box-shadow:2px 3px 8px rgba(0,0,0,.25);overflow:hidden}
.page--front{left:58px}
.page--inner{left:620px}
.sidebar{position:absolute;left:0;top:0;width:224px;height:100%;background:var(--blue)}
.portrait{position:absolute;left:18px;top:52px;width:192px;height:192px;border-radius:50%;border:4px solid #fff;background:radial-gradient(circle at 50% 40%,#d9b7a4 0,#b08a78 30%,#3a3a3f 62%,#cfd3d8 63%,#e7e9ec 100%)}
.nameplate{position:absolute;left:0;top:318px;width:228px;height:68px;background:var(--grey);padding:8px 0 0 20px}
.nameplate h1{font-family:'Roboto Condensed',sans-serif;font-weight:700;font-size:21px;color:var(--ink);line-height:1.1}
.nameplate p{font-size:8px;color:var(--ink);margin-top:5px;line-height:1.9}
.contact{position:absolute;left:20px;top:450px;list-style:none}
.contact li{font-weight:700;font-size:10.5px;color:#fff;height:29px;white-space:nowrap}
.contact b{color:var(--ink)}
.main{position:absolute;left:243px;top:20px;width:250px}
.title{font-family:'Roboto Condensed',sans-serif;font-weight:700;font-size:29px;color:var(--blue);line-height:1.1}
.subtitle{font-family:'Roboto Condensed',sans-serif;font-weight:400;font-size:27px;color:var(--ink);line-height:1.15;margin-bottom:12px}
.main-body{margin-left:7px;width:241px}
.bullets{list-style:none}
.bullets li{position:relative;padding-left:8px;font-size:7.6px;line-height:1.3;margin-bottom:3.4px;text-align:justify}
.bullets li::before{content:"";position:absolute;left:0;top:3px;width:4px;height:4px;border-radius:50%;background:var(--blue)}
.bullets li.plain::before{display:none}
.employer{margin:7px 0 3px}
.employer h2{font-weight:700;font-size:11.5px;color:var(--blue)}
.employer p{font-size:7.6px;line-height:1.3}
.footer{position:absolute;bottom:0;height:29px;background:var(--band);color:#fff;font-size:11px;letter-spacing:8px;display:flex;align-items:center;justify-content:center}
.page--front .footer{left:224px;right:0}
.page--inner .footer{left:0;right:0}
.cols{position:absolute;left:25px;width:465px;display:flex;gap:30px}
.cols .bullets{flex:1}
.cols .bullets li{font-size:7.8px}
.grey-zone{position:absolute;left:0;right:0;background:var(--grey)}
.tab{position:absolute;left:0;top:180px;width:162px;height:26px;background:var(--blue);color:#fff;font-weight:700;font-size:11px;padding:6px 0 0 22px}
.firm{position:absolute;left:0;top:409px;width:238px;height:70px;background:var(--blue);color:#fff;font-size:7.4px;font-weight:700;line-height:1.35;padding:10px 10px 0 20px}
.firm p+p{margin-top:4px}
.duty{position:absolute;left:32px;top:620px;font-size:7.6px;line-height:1.3}
.duty h3{font-weight:400;font-size:10px;color:var(--blue);margin-bottom:5px}
.duty p{margin-bottom:7px}
</style>
</head>
<body>

<section class="page page--front">
  <aside class="sidebar">
    <div class="portrait" role="img" aria-label="Porträtfoto des Bewerbers im Anzug"></div>
    <ul class="contact">
      <li><b>Adresse:</b> Lindenweg 4 10115 Berlin</li>
      <li><b>Geburtsdaten:</b> 14. Juli 1979 in Konstanz</li>
      <li><b>Familienstand:</b> verheiratet | 2 Kinder</li>
      <li><b>Mobile:</b>&nbsp;&nbsp; +49 (0) 170 55 2048 19</li>
      <li><b>E-Mail:</b> kontakt@weidner-mail.de</li>
      <li><b>Profil</b>https://www.netzprofil.de/jweidner</li>
    </ul>
  </aside>
  <div class="nameplate">
    <h1>Dr. Jonas Weidner</h1>
    <p>Chief Information Officer (CIO)<br>Ph.D. Wirtschaftsinformatik</p>
  </div>

  <div class="main">
    <div class="title">Chief Digital Officer</div>
    <div class="subtitle">Digital Leader</div>
    <div class="main-body">
      <ul class="bullets">
        <li>Kommunikationsstarke Führungspersönlichkeit mit mehrjähriger Erfahrung in Leitungsfunktionen im IT-Bereich, aktuell Chief Information Officer (CIO) und Chief Digital Officer (CDO)</li>
        <li>Umfangreiche Fachexpertise in: Konzeption und Weiterentwicklung von IT-Unternehmensstrategien | Effizienzsteigerung im IT-Bereich | Optimierung der IT-Service-Strukturen | Planung und Durchführung konzernweiter IT-Programme</li>
        <li>Experte auf dem Gebiet der Transformation von Unternehmen in die digitale Welt (Industrie 4.0) | Etablierung der IT als Business Enabler</li>
        <li>Führung von 75 MA + ca. 20 (weltweite und externe), davon 4 Führungskräfte | Budget i.H.v. 22 Mio. € p.a.</li>
        <li>Wissensmanager mit interkultureller Kompetenz, breitem Technologieverständnis sowie ausgeprägter Durchsetzungs- und Teamfähigkeit</li>
        <li class="plain">umsetzungsstark | lösungsorientiert | unternehmerisch | visionär</li>
      </ul>
      <div class="employer">
        <h2>Hartwig Gruppe</h2>
        <p>Balingen | www.hartwig-gruppe.de<br>Weltweiter Hersteller von zerspanenden Präzisionswerkzeugen | 6.400 MA weltweit in ca. 45 Ländern | 820 Mio. € Umsatz</p>
      </div>
      <ul class="bullets">
        <li>Verantwortung der operativen sowie strategischen IT weltweit</li>
        <li>Verantwortung der digitalen Transformation der Firma weltweit, Umsetzung der Vision Hartwig 2020</li>
        <li>Aufbau einer IT-Strategie in Abstimmung mit Geschäftsführung und Eigentümer</li>
        <li>Entwicklung und Umsetzung einer ERP-Roadmap 2020, inkl. Einführung Corvex Prime, Einführung Corvex Business Start in ca. 40 Tochtergesellschaften weltweit</li>
        <li>Aufbau eines IT-Risikomanagementsystems in Zusammenhang mit IT-GRC-Strukturen</li>
        <li>Definition einer zentralen e-Business Multichannel Architektur</li>
        <li>Aufbau einer IT-Leistungsrechnung sowie eines IT-Controllings</li>
        <li>Aufbau zweier IT Hubs in Asien und Amerika</li>
        <li>Neuausrichtung der gesamten IT-Infrastruktur (Migration von Nevaro zu Clearhaven)</li>
        <li>Etablierung einer IT-Projektmethodik</li>
        <li>Erarbeitung eines ECM-Konzepts „Just-in-time Informationslogistik“</li>
        <li>Definition/Rollout einer Prozessmodellierungssystematik unter BPMN 2.0 und Procivo</li>
        <li>Aufteilung der IT in Projektgeschäft und Katalog bzw. Standardgeschäft (vom Einkauf über Anforderungen bis hin zum Betrieb)</li>
        <li>Definition einer neuen IT-Organisation nach dem Plan-Build-Run Prinzip von ITIL</li>
        <li>Entwicklung einer Roadmap Industrie 4.0, Erprobung diverser Industrie-4.0-Themen mit der Produktion, Erarbeitung einer IT-Security-Strategie für alle Produktionswerke, Testen von neuen „Wearables“ zum Einsatz in der Produktion, Vollautomatisierung von Produktionswerken durch IT,</li>
      </ul>
    </div>
  </div>
  <div class="footer">www.nordhaus.com</div>
</section>

<section class="page page--inner">
  <div class="cols" style="top:46px">
    <ul class="bullets">
      <li>Aufbau einer neuen digitalen Einheit zur Erarbeitung von neuen Geschäftsmodellen</li>
      <li>Verantwortung: Führung von 75 MA + ca. 20 (weltweite und externe), davon 4 Führungskräfte | Budget i.H.v. 22 Mio. € Erfolge:</li>
      <li>Einführung einer globalen ERP-Strategie, Einsparung von 1/3 der Kosten bei jedem Rollout durch Einsatz der Mittelstandslösung Corvex-Business-Start, Verkürzung der Einführungszeiten von 1 Jahr auf 4 Monate sowie Erhöhung der Userzufriedenheit durch größere Usability und Simplicity der ERP Anwendung</li>
    </ul>
    <ul class="bullets">
      <li>Erstellung und Umsetzung einer globalen IT-Strategie und komplette Neustrukturierung der IT zu einer schnelleren und agileren Arbeitsweise (Etablierung einer Two Speed IT)</li>
      <li>Erstellung einer digitalen Vision Hartwig 2020</li>
      <li>Erzielung erster Online-Umsätze mit dem neuen eBusiness Konzept</li>
    </ul>
  </div>

  <div class="grey-zone" style="top:192px;height:217px"></div>
  <div class="tab">Chief Information Officer</div>
  <div class="cols" style="top:220px">
    <ul class="bullets">
      <li>Weltweite operative und strategische IT-Verantwortung</li>
      <li>Aufbau einer IT-Strategie in Abstimmung mit den beiden Gesellschaftern</li>
      <li>Integration verschiedener Nordhaus Standorte in die Gruppen-IT (linz, suzhou, brno)</li>
      <li>Projektverantwortlicher für die weltweite Einführung des ERP-Systems Varnex</li>
      <li>Definition von Anpassungsprogrammierungen und Erstellung von Konzepten für die eigenen ERP-Entwickler</li>
      <li>Entwicklung neuer Hardwarestrategien, u.a. Einführung von MFD-Geräten</li>
      <li>Aufbau eines Notfall- und Hochverfügbarkeitskonzepts für die gruppenweite IT</li>
      <li>Entwicklung einer gruppenweiten IT-policy und IT-Umweltstrategie</li>
    </ul>
    <ul class="bullets">
      <li>Aufbau von Servicestrukturen nach ITIL und Einführung eines Ticketingsystems (Servadesk)</li>
      <li>Verantwortung: Führung von 10 MA, davon 1 Führungskraft | Budget i.H.v. 4 Mio. € Erfolge:</li>
      <li>Neuausrichtung der IT, Erstellung einer globalen IT-Strategie</li>
      <li>Einführung eines neuen ERP-Systems</li>
      <li>Senkung der Printkosten innerhalb der gesamten Gruppe um ca. 50 % durch die Einführung einer globalen Printmanagementlösung</li>
      <li>Erhöhung der Anwenderzufriedenheit von Schulnote 3 auf 2+</li>
    </ul>
  </div>

  <div class="firm">
    <p>Kaltwerk Bus Europe | Leonberg |<br>(heute Brennhoff Klimasysteme GmbH &amp; Co. KG)</p>
    <p>Klimaanlagen für Omnibusse und Sonderfahrzeuge<br>| 180 MA</p>
  </div>

  <div class="cols" style="top:502px">
    <ul class="bullets">
      <li>IT-Verantwortung für alle EMEA-Standorte</li>
      <li class="plain">Entwicklung einer neuen IT-Strategie in Abstimmung mit der Corporate IT des Gesamtkonzerns</li>
      <li>Umsetzung der Corporate IT-Richtlinien, u.a. SOX</li>
      <li class="plain">Mitglied im globalen Projektteam „Einführung Corvex“</li>
      <li>Umsetzung eines Prozessberatungsprojekts innerhalb des Unternehmens</li>
    </ul>
    <ul class="bullets">
      <li>Projekt zur Erhöhung des Nutzungsgrades der ERP-Anwendung</li>
      <li>Releasewechsel des 10 Jahre alten ERP-Systems</li>
      <li class="plain">Einführung einer Opensource Reporting Lösung mit Quillo Reports</li>
      <li>Mitglied des sechsköpfigen Managementboards</li>
      <li class="plain">Planung und Konzeption von Change Requests für das ERP-System</li>
    </ul>
  </div>

  <div class="grey-zone" style="top:600px;height:92px"></div>
  <div class="duty">
    <h3>Verantwortung:</h3>
    <p>Führung von 4 MA | Budget i.H.v.</p>
    <p>2 Mio. € Erfolge:</p>
  </div>
  <div class="cols" style="top:612px;left:272px;width:218px">
    <ul class="bullets">
      <li>Prozessoptimierungen und Einsparungen in allen Unternehmensbereichen sowie Upgrade des bestehenden ERP Systems</li>
      <li>Erhöhung der Anwenderzufriedenheit von Schulnote 4 auf 1,5</li>
      <li>Senkung der IT-Kosten um 20%</li>
    </ul>
  </div>

  <div class="footer">www.nordhaus.com</div>
</section>

</body>
</html>
```